Business Card Design

my company buys cars,boats and caravans off the public, and also assists the public in helping them sell there item(brokering),i have an idea of a logo which is.....T$A....THE S BEING A LARGE DOLLAR SIGN,centred. And underneath my business name....TRADER-HOLDER-AGENT,i like black backgrounds, CLEAN SHARP AND TO THE POINT!!

Industry/Entity Type

Business

Contact Information for Business Card

$wap NOWLY.........buyer,seller,broker......cars,boats,caravans...........0427591846.......-swapnowly@traderholderagent.com.au, lmct-58417

Requirements
Must have
• MOBILE NUMBER-0427591846
EMAIL-swapnowly@traderholderagent.com.au
business name-TRADER-HOLDER-AGENT
lmct-58417
what we deal in-Cars,Caravans,Boats
cash,bank chq, finance paid out
Nice to have
• clever logo created by you guys

```html
<!DOCTYPE html>
<html lang="en">
<head>
<meta charset="utf-8">
<title>TRADER-HOLDER-AGENT Business Cards</title>
<link rel="stylesheet" href="https://fonts.googleapis.com/css2?family=Alegreya:wght@400&display=swap">
<style>
  :root {
    --backdrop: #2b2b2d;
    --card-black: #050505;
    --card-white: #ececec;
    --ink-light: #f2f2f2;
    --ink-dark: #1a1a1a;
  }
  * { margin: 0; padding: 0; box-sizing: border-box; }
  html, body {
    width: 1200px;
    height: 800px;
    overflow: hidden;
    background: var(--backdrop);
  }
  .canvas {
    width: 1200px;
    height: 800px;
    display: flex;
    align-items: center;
    justify-content: center;
    gap: 40px;
    font-family: "Alegreya", Georgia, serif;
    font-weight: 400;
  }
  .card {
    width: 540px;
    height: 309px;
    position: relative;
    overflow: hidden;
    box-shadow: 0 14px 30px rgba(0,0,0,0.45);
    text-align: center;
  }
  .card--dark { background: var(--card-black); color: var(--ink-light); }
  .card--split { background: var(--card-white); color: var(--ink-dark); }
  .card__band {
    position: absolute;
    left: 0; top: 0;
    width: 100%;
    height: 128px;
    background: var(--card-black);
  }
  .brand {
    position: absolute;
    left: 0;
    width: 100%;
    top: 50px;
    color: var(--ink-light);
    font-size: 24px;
    letter-spacing: 2px;
    line-height: 1;
  }
  .details {
    position: absolute;
    left: 0;
    width: 100%;
    top: 140px;
    font-size: 14px;
    line-height: 1.35;
  }
  .details__business {
    font-size: 17px;
    letter-spacing: 0.5px;
    margin-bottom: 1px;
  }
  .details__offer { margin-bottom: 6px; }
  .details__phone { letter-spacing: 1px; margin-bottom: 6px; }
</style>
</head>
<body>
<main class="canvas">

  <section class="card card--dark" aria-label="Business card, black version">
    <p class="brand">TRADER-HOLDER-AGENT</p>
    <div class="details">
      <p class="details__business">TRADER-HOLDER-AGENT</p>
      <p>We deal in:</p>
      <p class="details__offer">Cars, Caravans, Boats - Cash, Bank chq, Finance paid out</p>
      <p class="details__phone">0427591846</p>
      <p>swapnowly@traderholderagent.com.au</p>
      <p>lmct-58417</p>
    </div>
  </section>

  <section class="card card--split" aria-label="Business card, black and white version">
    <div class="card__band"></div>
    <p class="brand">TRADER-HOLDER-AGENT</p>
    <div class="details">
      <p class="details__business">TRADER-HOLDER-AGENT</p>
      <p>We deal in:</p>
      <p class="details__offer">Cars, Caravans, Boats - Cash, Bank chq, Finance paid out</p>
      <p class="details__phone">0427591846</p>
      <p>swapnowly@traderholderagent.com.au</p>
      <p>lmct-58417</p>
    </div>
  </section>

</main>
</body>
</html>
```